Poster for a an ad on Facebook and website

Event is a hot rod..cool car cruise across Southern Ontario on September 21st and 22nd see www.lakeshoremotorparade7.com ad is to catch people's eyes and make them want to join in the Cruise. Two examples are included as ideas..folks travel from the PHOTOBOOTH's in Fort Erie and St.Thomas where they have had thier phots taken..small car gatherings break out at stops all along the 225km route..

Target Market(s)

car enthusiasts

Industry/Entity Type

automotive ..hot rods collector cars

Requirements
Must have
• Dates and a cool look--KTR presents sponsor logo as attached
Nice to have
• incorporate Hwy#3..thats the route

```html
<!DOCTYPE html>
<html lang="en">
<head>
<meta charset="utf-8">
<title>Motor Parade VII – Hot Rod Cruise Poster</title>
<link rel="stylesheet" href="https://fonts.googleapis.com/css2?family=Oswald:wght@500&family=UnifrakturMaguntia&display=swap">
<style>
  :root {
    --sunset-orange: #d68a55;
    --lake-blue: #5465a0;
    --ink: #0b0b0c;
    --paper: #ffffff;
    --chrome-dark: #1c1c20;
    --chrome-mid: #45454d;
    --font-display: "Oswald", "Arial Narrow", sans-serif;
    --font-blackletter: "UnifrakturMaguntia", "Old English Text MT", serif;
  }
  html, body {
    margin: 0;
    padding: 0;
    width: 947px;
    height: 1200px;
    overflow: hidden;
    background: var(--paper);
  }
  .poster {
    position: relative;
    width: 947px;
    height: 1200px;
  }
  .poster-art {
    display: block;
    width: 947px;
    height: 1200px;
  }
  .display-type { font-family: var(--font-display); font-weight: 500; }
  .blackletter { font-family: var(--font-blackletter); }
</style>
</head>
<body>
<main class="poster">
  <svg class="poster-art" viewBox="0 0 947 1200" xmlns="http://www.w3.org/2000/svg">
    <defs>
      <path id="arc-top" d="M196,300 Q476,150 758,300"/>
      <path id="arc-bottom" d="M236,468 Q476,560 716,468"/>
      <linearGradient id="hotrod-tone" x1="0" y1="0" x2="1" y2="1">
        <stop offset="0" stop-color="var(--chrome-mid)"/>
        <stop offset="1" stop-color="var(--chrome-dark)"/>
      </linearGradient>
    </defs>

    <!-- backdrop bands -->
    <g class="backdrop">
      <rect class="band-sky" x="37" y="46" width="878" height="559" fill="var(--sunset-orange)"/>
      <rect class="band-road" x="37" y="604" width="878" height="556" fill="var(--lake-blue)"/>
      <rect class="frame" x="37" y="46" width="878" height="1114" fill="none" stroke="var(--ink)" stroke-width="3"/>
    </g>

    <!-- title badge -->
    <g class="title-badge">
      <ellipse cx="476" cy="362" rx="400" ry="197" fill="var(--ink)"/>
      <ellipse cx="476" cy="362" rx="383" ry="182" fill="none" stroke="var(--paper)" stroke-width="1.6"/>
      <text class="blackletter" font-size="44" fill="var(--paper)" text-anchor="middle">
        <textPath href="#arc-top" startOffset="50%">Ontario’s Lakeshore</textPath>
      </text>
      <text class="badge-star" x="186" y="296" font-size="14" fill="var(--paper)" text-anchor="middle">✪</text>
      <text class="badge-star" x="758" y="296" font-size="14" fill="var(--paper)" text-anchor="middle">✪</text>
      <text class="display-type event-title" x="476" y="418" font-size="128" fill="var(--paper)" text-anchor="middle" textLength="693" lengthAdjust="spacingAndGlyphs">MOTOR PARADE VII</text>
      <text class="blackletter" font-size="27" fill="var(--paper)" text-anchor="middle">
        <textPath href="#arc-bottom" startOffset="50%">Where classics meet the open road</textPath>
      </text>
      <text class="badge-star" x="236" y="482" font-size="13" fill="var(--paper)" text-anchor="middle">✪</text>
      <text class="badge-star" x="716" y="482" font-size="13" fill="var(--paper)" text-anchor="middle">✪</text>
    </g>

    <!-- hero vehicle -->
    <rect class="hero-hotrod" x="156" y="542" width="640" height="376" rx="60" fill="url(#hotrod-tone)" role="img" aria-label="Black and white illustration of a supercharged 1930s hot rod coupe with exposed V8 engine and chrome wheels"/>

    <!-- date plate -->
    <g class="date-plate">
      <rect x="600" y="724" width="262" height="150" rx="14" fill="var(--ink)"/>
      <rect x="593" y="717" width="262" height="150" rx="14" fill="var(--paper)" stroke="var(--ink)" stroke-width="5"/>
      <text class="display-type" x="724" y="777" font-size="58" fill="var(--ink)" text-anchor="middle">SEPT</text>
      <text class="blackletter" x="724" y="842" font-size="66" fill="var(--ink)" text-anchor="middle">21<tspan font-size="20" dy="-38">st</tspan><tspan font-size="40" dy="30"> &amp; </tspan><tspan font-size="66" dy="8">22</tspan><tspan font-size="20" dy="-38">nd</tspan></text>
      <polygon points="609,793 613,789 618,793 613,797" fill="var(--ink)"/>
      <polygon points="830,793 835,789 840,793 835,797" fill="var(--ink)"/>
    </g>

    <!-- sponsor bar -->
    <g class="sponsor-bar">
      <path d="M37,975 H440 a58,58 0 0 1 58,58 v13 a58,58 0 0 1 -58,58 H37 Z" fill="var(--ink)"/>
      <path d="M37,985 H432 a50,50 0 0 1 50,50 v9 a50,50 0 0 1 -50,50 H37" fill="none" stroke="var(--paper)" stroke-width="1.6"/>
      <text class="display-type sponsor-name" x="60" y="1064" font-size="62" fill="var(--paper)">KTR</text>
      <text class="display-type sponsor-name" x="228" y="1055" font-size="34" fill="var(--paper)">NORTHLINE PARTS</text>
    </g>

    <!-- route -->
    <g class="route-map">
      <text class="blackletter" x="598" y="988" font-size="34" fill="var(--paper)" text-anchor="middle">Fort</text>
      <text class="blackletter" x="598" y="1024" font-size="34" fill="var(--paper)" text-anchor="middle">Erie</text>
      <text class="blackletter" x="821" y="988" font-size="34" fill="var(--paper)" text-anchor="middle">St.</text>
      <text class="blackletter" x="821" y="1024" font-size="34" fill="var(--paper)" text-anchor="middle">Thomas</text>
      <g fill="none" stroke="var(--ink)" stroke-width="4">
        <circle cx="598" cy="1038" r="8" fill="var(--paper)"/>
        <circle cx="818" cy="1038" r="8" fill="var(--paper)"/>
        <path d="M598,1046 V1090 H612"/>
        <path d="M818,1046 V1090 H804"/>
        <path d="M616,1090 H802" stroke-dasharray="9 6"/>
      </g>
      <text class="display-type route-distance" x="717" y="1133" font-size="24" fill="var(--paper)" text-anchor="middle">225 KM</text>
    </g>
  </svg>
</main>
</body>
</html>
```